Marketing Company Needs Creative Brochure Design

We need a brochure design for a new company based in the Twin Cities called 'Lanternway Marketing'. We work with our clients to get them found on the internet and at the top of Zorvex page rankings. We offer a variety of marketing tools for our clients from Search Engine Optimization (SEO), to social media, videos, blogs, article marketing, etc... We would like to incorporate the blacksmith theme. Our colors are red and black. The final design should communicate business growth.

Target Market(s)

business owners

Industry/Entity Type

Marketing

Requirements
Should not have
• Although we would like to incorporate the blacksmith theme, please don't make it cheesy. Think sophistication and creativity.

```html
<!DOCTYPE html>
<html lang="en">
<head>
<meta charset="utf-8">
<title>Lanternway Marketing – Web Presence</title>
<link href="https://fonts.googleapis.com/css2?family=Graduate&family=Carlito:wght@400;700&family=Roboto+Slab:wght@800&family=Oswald:wght@700&display=swap" rel="stylesheet">
<style>
  :root {
    --ink: #111111;
    --red: #c8232c;
    --page-light: #dcdcdc;
    --page-dark: #8c8c8c;
    --footer-grey: #4a4a4a;
    --white: #ffffff;
    --stage: #000000;
  }
  * { margin: 0; padding: 0; box-sizing: border-box; }
  html, body { width: 1200px; height: 900px; overflow: hidden; background: var(--stage); }
  .spread { position: absolute; left: 37px; top: 87px; width: 1126px; height: 728px; }
  .page-left {
    position: absolute; left: 0; top: 0; width: 563px; height: 728px;
    background: linear-gradient(180deg, var(--page-light) 0%, #c4c4c4 45%, var(--page-dark) 100%);
  }
  .photo-team {
    position: absolute; left: 563px; top: 0; width: 563px; height: 728px;
    background: linear-gradient(160deg, #e4c2bd 0%, #c99590 45%, #8e4d48 80%, #5e2a27 100%);
  }
  .section-title {
    position: absolute; left: 0; width: 583px; top: 88px; text-align: center;
    font-family: "Graduate", "Roboto Slab", serif; font-weight: 400; font-size: 40px;
    line-height: 52px; color: var(--red); letter-spacing: 0;
    -webkit-text-stroke: 1.2px var(--red);
  }
  .tagline {
    position: absolute; left: 66px; width: 452px; top: 147px; padding: 2px 0 3px;
    border-top: 2px solid var(--red); border-bottom: 2px solid var(--red);
    text-align: center; font-family: "Graduate", "Roboto Slab", serif; font-weight: 400;
    font-size: 20px; line-height: 24px; color: var(--ink);
    -webkit-text-stroke: 0.5px var(--ink);
  }
  .body-copy {
    position: absolute; left: 66px; top: 220px; width: 470px;
    font-family: "Carlito", "Calibri", sans-serif; font-size: 14.3px; line-height: 19.4px;
    color: var(--ink); white-space: nowrap;
  }
  .body-copy p { margin-bottom: 9.6px; }
  .strategies-title { font-weight: 700; }
  .strategies { list-style: none; }
  .strategies li { line-height: 19.4px; }
  .strategies li::before {
    content: ""; display: inline-block; width: 7px; height: 7px; border-radius: 50%;
    background: var(--red); margin-right: 5px; vertical-align: 1px;
  }
  .folio { position: absolute; top: 685px; height: 24px; display: flex; align-items: center; }
  .folio-left { left: 0; }
  .folio-right { right: 0; flex-direction: row-reverse; }
  .folio-tab { width: 25px; height: 24px; background: var(--red); }
  .folio-number {
    font-family: "Oswald", sans-serif; font-weight: 700; font-size: 28px; line-height: 24px;
    color: var(--white); margin: 0 11px 0 12px;
  }
  .folio-right .folio-number { margin: 0 12px 0 10px; }
  .folio-name {
    font-family: "Roboto Slab", serif; font-weight: 800; font-size: 11px;
    color: var(--footer-grey); letter-spacing: 0.3px;
  }
</style>
</head>
<body>
<div class="spread">
  <section class="page-left">
    <h1 class="section-title">WEB PRESENCE</h1>
    <h2 class="tagline">“WE USE THE BEST AND MOST RELEVANT<br>KEYWORDS FOR YOUR BUSINESS”</h2>
    <div class="body-copy">
      <p>Your company is a little fish in a big pond on the World Wide Web. Let<br>us highlight your company and bring it to the surface. Our team is highly<br>knowledgeable in Search Engine Optimization, or the craft of getting<br>you listed high and on the front page of search results so that potential<br>clients can find you. We use the best and most relevant keywords for your<br>business, and we create a plan to optimize your site for these keywords.<br>Search Engine Optimization is constantly evolving, and we are always<br>working to stay ahead of the trends to provide the best service to our<br>clients. When you appear higher in search results, a larger volume of<br>people will visit your site and discover your business – it’s as simple as that.</p>
      <p>Your website is a powerful tool used to communicate with potential<br>clients. Make sure you are sending the right message at first click!We can<br>professionally design custom websites full of engaging content and an<br>intuitive navigation system that captures leads by offering incentives to<br>potential clients. We can also work with you to optimize your current site to<br>ensure that your site is search engine-friendly.</p>
      <div class="strategies-title">Strategies</div>
      <ul class="strategies">
        <li>Conduct Thorough Keyword Research</li>
        <li>Acquire Strategic Domain Name</li>
        <li>Build Organic Search Results</li>
        <li>Create Key Online Directories Profiles</li>
        <li>Pay Per Click Campaign Management</li>
      </ul>
    </div>
    <div class="folio folio-left">
      <span class="folio-tab"></span>
      <span class="folio-number">6</span>
      <span class="folio-name">LANTERNWAY MARKETING</span>
    </div>
  </section>
  <section class="photo-team" role="img" aria-label="Red-toned photo of four business people gathered around a laptop, smiling at the screen">
    <div class="folio folio-right">
      <span class="folio-tab"></span>
      <span class="folio-number">7</span>
      <span class="folio-name">LANTERNWAY MARKETING</span>
    </div>
  </section>
</div>
</body>
</html>
```